Hip-Hop/Rap album needs artwork

I would like a design that parallels the ideas of beauty and flaws. My name is Rohan Mehta and I'm titling it "Hollow Embers", this album is basically a collection of songs that have me trying to understand the good and evil in this world, how they run so close together at times. How they sometimes can be caused by the same source, or how sometimes we find beauty within all the ugliness we witness. Some subject matters include rape, serial killers, depression, the idea of love, the projection of women in the media, and the idea of dying prematurely.

Target Market(s)

Music listeners, who are looking for new music so artwork that will capture their eye and stand out, rough age estimate would be 17-35, people with time to kill.

Industry/Entity Type

Media

Font styles to use
Decorative
Script

Requirements
Must have
• please include my name ROHAN MEHTA and the title HOLLOW EMBERS, preferably in different fonts

I'm going for something more moody and dark rather than something happy, so darker colors please.
Nice to have
• I would prefer to have a drawing or painting of some sort, to give some humanity to the design but not required.

```html
<!DOCTYPE html>
<html lang="en">
<head>
<meta charset="utf-8">
<title>Rohan Mehta — Hollow Embers</title>
<link rel="stylesheet" href="https://fonts.googleapis.com/css2?family=Federo&family=Cinzel:wght@400&display=swap">
<style>
  :root {
    --navy-deep: #07122e;
    --navy: #12306a;
    --teal-dark: #164f55;
    --teal: #1d6a62;
    --sea-green: #3a8466;
    --moss: #6a9c5c;
    --ember-gold: #d9b46a;
    --ember-peach: #e9b884;
    --title-grey: #d4d4d4;
    --subtitle-white: #f4f4f4;
  }

  html, body {
    margin: 0;
    padding: 0;
    width: 1200px;
    height: 1200px;
    overflow: hidden;
    background: var(--navy-deep);
  }

  .album-cover {
    position: relative;
    width: 1200px;
    height: 1200px;
    overflow: hidden;
  }

  .cover-artwork {
    position: absolute;
    inset: 0;
    background:
      radial-gradient(ellipse 22% 9% at 72% 52%, rgba(233, 184, 132, 0.8), rgba(233, 184, 132, 0) 100%),
      radial-gradient(ellipse 14% 16% at 42% 40%, rgba(217, 180, 106, 0.55), rgba(217, 180, 106, 0) 100%),
      radial-gradient(ellipse 10% 8% at 18% 58%, rgba(217, 180, 106, 0.35), rgba(217, 180, 106, 0) 100%),
      linear-gradient(28deg, rgba(7, 18, 46, 0) 0%, rgba(7, 18, 46, 0) 56%, rgba(18, 48, 106, 0.55) 62%, rgba(7, 18, 46, 0) 70%),
      linear-gradient(-12deg, rgba(7, 18, 46, 0) 30%, rgba(18, 48, 106, 0.6) 36%, rgba(7, 18, 46, 0) 44%),
      radial-gradient(ellipse 60% 50% at 50% 45%, var(--moss) 0%, var(--sea-green) 35%, rgba(29, 106, 98, 0) 80%),
      linear-gradient(90deg, rgba(7, 18, 46, 0) 65%, rgba(7, 18, 46, 0.85) 100%),
      linear-gradient(180deg, var(--teal) 0%, var(--teal-dark) 55%, var(--navy) 75%, var(--teal-dark) 100%);
  }

  .artwork-grain {
    position: absolute;
    inset: 0;
    width: 1200px;
    height: 1200px;
    mix-blend-mode: overlay;
    opacity: 0.55;
  }

  .artist-name {
    position: absolute;
    top: 40px;
    left: 0;
    width: 100%;
    margin: 0;
    text-align: center;
    white-space: nowrap;
    font-family: "Federo", "Poiret One", sans-serif;
    font-weight: 400;
    font-size: 150px;
    line-height: 1;
    letter-spacing: 4px;
    color: var(--title-grey);
  }

  .artist-name-text {
    display: inline-block;
    transform: scaleX(0.7);
    transform-origin: center;
  }

  .album-title {
    position: absolute;
    top: 1092px;
    left: 0;
    width: 100%;
    margin: 0;
    padding-left: 30px;
    box-sizing: border-box;
    text-align: center;
    white-space: nowrap;
    font-family: "Cinzel", serif;
    font-weight: 400;
    font-size: 38px;
    line-height: 1;
    letter-spacing: 30px;
    color: var(--subtitle-white);
  }
</style>
</head>
<body>
  <main class="album-cover">
    <div class="cover-artwork" role="img" aria-label="Abstract painted texture in deep teal, sea green and navy, with dark diagonal bands and a glowing golden-peach ember at the centre"></div>
    <svg class="artwork-grain" viewBox="0 0 1200 1200" aria-hidden="true">
      <filter id="paint-grain">
        <feTurbulence type="fractalNoise" baseFrequency="0.012 0.02" numOctaves="5" seed="7"/>
        <feColorMatrix type="saturate" values="0"/>
      </filter>
      <rect width="1200" height="1200" filter="url(#paint-grain)"/>
    </svg>
    <h1 class="artist-name"><span class="artist-name-text">ROHAN MEHTA</span></h1>
    <h2 class="album-title">HOLLOW EMBERS</h2>
  </main>
</body>
</html>
```